Updated Business Cards

We need to update our business cards to reflect new services and employees. We are a luxury vacation rental company in Sandpoint, Idaho. Would also like to make the front facing font easier to read (larger fonts) I love the original logo created for our company and want to use this for the back of the business card created like before - with the dark blue color. See previous files.

Front of the card needs to include:
Employee Name
Title
Phone: 555-555-0147 (ext X)
Address: 418 W. Larkmoor St, Ste 5
Willowbay, WA 83871
Book Direct: www.RestWillowbay.example

```html
<!DOCTYPE html>
<html lang="en">
<head>
<meta charset="utf-8">
<title>Hartwell Management – Business Cards</title>
<link rel="stylesheet" href="https://fonts.googleapis.com/css2?family=Cinzel:wght@500&family=Montserrat:wght@700&family=Roboto:wght@400&display=swap">
<style>
  :root {
    --backdrop: #e6e7ea;
    --navy: #0a2a78;
    --navy-deep: #07205f;
    --navy-soft: #1d3f8e;
    --card-white: #f2f2f2;
    --ink-grey: #5f6166;
    --rule-grey: #9a9ca1;
    --white: #ffffff;
  }
  * { box-sizing: border-box; margin: 0; padding: 0; }
  html, body { width: 1200px; height: 900px; overflow: hidden; }
  body {
    background: var(--backdrop);
    position: relative;
    font-family: "Roboto", Arial, sans-serif;
  }
  .card {
    position: absolute;
    width: 600px;
    height: 343px;
    border-radius: 28px;
    overflow: hidden;
    box-shadow: 0 10px 28px rgba(0,0,0,0.18);
  }

  /* Back of card */
  .card--back { left: 60px; top: 60px; }
  .card--back .scenery {
    position: absolute; inset: 0;
    background: linear-gradient(160deg, var(--navy) 0%, var(--navy-deep) 55%, var(--navy-soft) 100%);
  }
  .card--back .brand {
    position: absolute; inset: 0;
    display: flex; flex-direction: column; align-items: center; justify-content: center; gap: 20px;
  }
  .brand-dot {
    width: 64px; height: 64px; border-radius: 50%;
    background: var(--white);
  }
  .card--back .brand-name {
    font-family: "Cinzel", Georgia, serif;
    font-weight: 500;
    font-size: 40px;
    letter-spacing: 2px;
    color: var(--white);
  }

  /* Front of card */
  .card--front { left: 540px; top: 497px; background: var(--card-white); }
  .front-brand {
    position: absolute; top: 38px; left: 0; right: 0;
    display: flex; align-items: center; justify-content: center; gap: 16px;
  }
  .front-brand .brand-dot { width: 44px; height: 44px; background: var(--navy); }
  .front-brand .brand-name {
    font-family: "Cinzel", Georgia, serif;
    font-weight: 500; font-size: 32px; letter-spacing: 1px;
    color: var(--navy);
  }
  .person {
    position: absolute; left: 24px; top: 148px; width: 226px;
    text-align: right;
  }
  .person-name {
    font-family: "Montserrat", Arial, sans-serif;
    font-weight: 700; font-size: 26px; color: var(--navy);
    letter-spacing: 0.5px;
  }
  .person-title { font-size: 20px; color: var(--ink-grey); margin-top: 4px; }
  .divider {
    position: absolute; left: 266px; top: 118px;
    width: 1px; height: 130px; background: var(--rule-grey);
  }
  .contacts {
    position: absolute; left: 284px; top: 128px;
    list-style: none; display: flex; flex-direction: column; gap: 12px;
    font-size: 17px; color: var(--ink-grey);
  }
  .contacts li, .address { display: flex; align-items: center; gap: 9px; }
  .icon { width: 17px; height: 17px; flex: none; fill: var(--navy); }
  .address {
    position: absolute; left: 0; right: 0; bottom: 40px; justify-content: center;
    font-size: 18px; color: var(--ink-grey);
  }
</style>
</head>
<body>

<section class="card card--back" aria-label="Card back">
  <div class="scenery" role="img" aria-label="Faint dark blue mountain and lake landscape photograph"></div>
  <div class="brand">
    <span class="brand-dot"></span>
    <span class="brand-name">Hartwell Management</span>
  </div>
</section>

<section class="card card--front" aria-label="Card front">
  <div class="front-brand">
    <span class="brand-dot"></span>
    <span class="brand-name">Hartwell Management</span>
  </div>

  <div class="person">
    <p class="person-name">OWEN MARSH</p>
    <p class="person-title">Managing Director</p>
  </div>

  <div class="divider"></div>

  <ul class="contacts">
    <li>
      <svg class="icon" viewBox="0 0 24 24"><path d="M6.6 10.8a15.1 15.1 0 0 0 6.6 6.6l2.2-2.2a1 1 0 0 1 1-.25 11.4 11.4 0 0 0 3.6.57 1 1 0 0 1 1 1V20a1 1 0 0 1-1 1A17 17 0 0 1 3 4a1 1 0 0 1 1-1h3.5a1 1 0 0 1 1 1c0 1.25.2 2.45.57 3.57a1 1 0 0 1-.25 1z"/></svg>
      555-555-0147 (ext X)
    </li>
    <li>
      <svg class="icon" viewBox="0 0 24 24"><path d="M2 5h20v2l-10 7L2 7z"/><path d="M2 9.4l10 7 10-7V19H2z"/></svg>
      info@RestWillowbay.example
    </li>
    <li>
      <svg class="icon" viewBox="0 0 24 24"><circle cx="12" cy="12" r="10"/></svg>
      www.RestWillowbay.example
    </li>
  </ul>

  <p class="address">
    <svg class="icon" viewBox="0 0 24 24"><path d="M12 2a7 7 0 0 0-7 7c0 5.2 7 13 7 13s7-7.8 7-13a7 7 0 0 0-7-7zm0 9.5A2.5 2.5 0 1 1 12 6.5a2.5 2.5 0 0 1 0 5z"/></svg>
    418 W. Larkmoor St, Ste 5 Willowbay, WA 83871
  </p>
</section>

</body>
</html>
```